GUARANTEED WordPress design needed for a sassy, confident charisma coach!

We need a website design for Marla Penrick's brand new, responsive, Wordpress website.
Marla is a trainer / coach who teaches people how to be more charismatic and runs events, publishes video courses and has an ongoing video blog. Her old website is here: www.marlapenrick.co.uk ... but it's now time to have a much better site!
We have a strong idea about the technical components of the website, but we need a designer's eye to create a great style for the site (and provide layered PSD files which our developers will then convert to HTML and CSS).
Marla's brand is sassy, brave, warm and confident. The videos on her existing site give quite a good feel for her personality. We need a clean, stylish and compelling page that isn't too corporate and captures her personality. Every element needs to feel coherent, from fonts and headings to colours and spacing.
The following sites are not exactly what Marla wants (and certainly aren't right in terms of colours) but they give you an idea of the kind of people she is competing against and the area she is operating in:
http://www.tessa-broughley.example/
http://rowanfelsby.example/
Ideally, you will have done something similar and be able to key in on exactly the kind of thing we want: we're not looking to reinvent the wheel. Hopefully you won't mind tweaking a few things if you are close to what we need.
More detail is provided in the word document attached. But in a nutshell we need: a banner, footer, sign-up strap, menu bar, signature and 4 different basic page types. We want bursts of bright colours, contrasted with black and white if possible - sorry we can't be more specific than that...
The word doc also contains some amateur mock-ups as well (the images are also just mockups at this stage) - but although these give a general sense of the structure what we are looking for, we are clearly not designers...so please help! We need a designer's touch!
Kind regards,
Corin
PS The layered PSD versions of the mockup files are available on Cloudvantre: https://files.cloudvantre.example/sh/k72pqa4w1zbtmrd/QXvenlr8Ty3PwMiU6Hs2kYfDb?dl=0
Target Market(s)
Entrepreneurs who need to sell themselves.
Number of Pages Required
4 page

```html
<!DOCTYPE html>
<html lang="en">
<head>
<meta charset="utf-8">
<title>Marla Penrick – Charisma Coach</title>
<link rel="stylesheet" href="https://fonts.googleapis.com/css2?family=Raleway:wght@400;600;700;800&family=Open+Sans:wght@400;600;700&display=swap">
<style>
:root{
  --teal:#18b4d0;
  --teal-dark:#0f9bb6;
  --red:#e3161d;
  --green:#7dc142;
  --cyan:#1fb6d6;
  --yellow:#f4c61c;
  --orange:#f7a21b;
  --ink:#2a2a2a;
  --grey:#8a8a8a;
  --page:#ececec;
  --white:#ffffff;
  --night:#2c2c2c;
}
*{box-sizing:border-box;margin:0;padding:0}
html,body{width:1200px;height:2508px;overflow:hidden}
body{position:relative;background:var(--page);font-family:"Open Sans",Arial,sans-serif;color:var(--ink)}
.site-header{position:absolute;top:0;left:0;width:1200px;height:88px;background:var(--white);display:flex;align-items:center;justify-content:space-between;padding:0 220px}
.brand{display:flex;align-items:center;gap:10px;font-family:"Raleway",sans-serif;font-weight:700;font-size:26px;color:var(--ink)}
.brand-dot{width:12px;height:12px;border-radius:50%;background:var(--teal)}
.main-nav{display:flex;gap:26px;font-family:"Raleway",sans-serif;font-weight:700;font-size:12px;letter-spacing:1px;color:var(--ink)}
.hero{position:absolute;top:88px;left:0;width:1200px;height:352px;background:linear-gradient(90deg,#e6f4f8 0%,#d2ecf3 45%,#c8e4ec 52%,#d94a4e 58%,#d8323a 64%,#cbe6ee 70%,#e4f3f7 100%)}
.hero-copy{position:absolute;top:178px;left:220px;font-family:"Raleway",sans-serif}
.hero-title{font-weight:800;font-size:44px;line-height:1;color:var(--ink)}
.hero-title span{display:block;color:var(--teal);font-size:56px;margin-top:4px}
.hero-text{margin-top:14px;width:300px;font-family:"Open Sans",sans-serif;font-size:12px;line-height:1.5;color:#555}
.hero-dots{display:flex;gap:8px;margin-top:16px}
.hero-dots i{width:14px;height:14px;border-radius:50%;background:var(--ink)}
.hero-dots i:first-child{background:var(--white);border:2px solid var(--ink)}
.signup-strap{position:absolute;top:440px;left:0;width:1200px;height:120px;background:linear-gradient(180deg,#3fc6dd,var(--teal));display:flex;align-items:center;padding:0 220px;gap:18px}
.strap-copy{color:var(--white);width:320px}
.strap-copy strong{display:block;font-family:"Raleway",sans-serif;font-size:17px;font-weight:600;line-height:1.3}
.strap-copy small{font-size:10px}
.strap-form{display:flex;flex-direction:column;gap:8px;margin-left:30px}
.field{width:130px;height:24px;background:var(--white);border-radius:2px;font-size:10px;color:#aaa;padding:5px 8px}
.signup-btn{width:78px;height:78px;border-radius:50%;background:var(--orange);color:var(--white);font-family:"Raleway",sans-serif;font-weight:800;font-size:15px;display:flex;align-items:center;justify-content:center;text-align:center;line-height:1.1;margin-left:24px}
.blog-panel{position:absolute;top:596px;left:220px;width:606px;height:1590px;background:var(--white);padding:24px 20px 0}
.post{height:380px}
.post-banner{position:relative;width:480px;height:200px;display:flex;overflow:hidden}
.banner-copy{flex:1;padding:22px 20px;font-family:"Raleway",sans-serif;color:var(--white);font-weight:700;font-size:22px;line-height:1.15}
.banner-copy b{display:block;font-weight:800;font-size:40px;margin-top:6px}
.banner-photo{width:170px;height:100%}
.banner-red{background:var(--red)}
.banner-green{background:var(--green)}
.banner-cyan{background:var(--cyan)}
.banner-yellow{background:var(--yellow)}
.banner-yellow .banner-copy,.banner-green .banner-copy{color:#1d1d1d}
.banner-cyan .banner-copy b{color:#ffe16b}
.post-title{margin-top:20px;font-family:"Raleway",sans-serif;font-weight:700;font-size:18px}
.post-excerpt{margin-top:8px;font-size:11px;line-height:1.55;color:var(--grey);width:540px}
.post-meta{margin-top:14px;width:560px;border-top:1px solid #e3e3e3;padding-top:10px;display:flex;justify-content:space-between;align-items:center}
.read-more{font-family:"Raleway",sans-serif;font-weight:700;font-size:11px;color:var(--teal)}
.shares{display:flex;gap:6px}
.shares i{width:38px;height:16px;border-radius:2px;background:#dfe6ee}
.shares i:nth-child(2){background:#d9eef8}
.shares i:nth-child(3){background:#f6dada}
.pagination{display:flex;justify-content:center;gap:4px;margin-top:-10px}
.pagination span{width:20px;height:20px;border:1px solid #ccc;font-size:10px;color:#777;display:flex;align-items:center;justify-content:center}
.pagination span.current{background:var(--teal);color:var(--white);border-color:var(--teal)}
.sidebar{position:absolute;top:596px;left:846px;width:126px}
.widget{background:var(--white);margin-bottom:40px}
.widget-title{font-family:"Raleway",sans-serif;font-weight:800;font-size:12px;color:var(--white);background:var(--orange);padding:8px 10px}
.widget-title.plain{background:var(--white);color:var(--ink);border-bottom:2px solid #eee}
.top-list{padding:6px 10px 10px}
.top-list li{list-style:none;font-size:9px;line-height:1.35;color:#666;padding:5px 0;border-bottom:1px solid #eee}
.top-list li em{display:block;font-style:normal;font-weight:700;color:var(--red);font-size:8px;margin-top:2px}
.tags{display:flex;flex-wrap:wrap;gap:4px;padding:10px}
.tags span{background:var(--red);color:var(--white);font-size:9px;font-weight:700;padding:2px 4px}
.event-card{position:relative;height:360px;background:linear-gradient(180deg,#6d5a4e,#3b302b 60%,#2d2522)}
.event-copy{position:absolute;left:10px;top:150px;color:var(--white);font-family:"Raleway",sans-serif;font-weight:800;font-size:15px;line-height:1.15}
.event-copy b{display:inline-block;margin-top:8px;background:var(--teal);font-size:24px;padding:2px 8px}
.event-copy small{display:block;font-size:9px;font-weight:600;margin-top:6px}
.learn-more{position:absolute;left:0;bottom:0;width:100%;height:42px;background:var(--orange);color:var(--white);font-family:"Raleway",sans-serif;font-weight:800;font-size:13px;display:flex;align-items:center;justify-content:center}
.site-footer{position:absolute;top:2190px;left:0;width:1200px;height:282px;background:var(--teal);text-align:center;color:var(--white);padding-top:44px}
.footer-pitch{font-family:"Raleway",sans-serif;font-size:17px;font-weight:600;line-height:1.5;width:620px;margin:0 auto}
.footer-form{display:flex;justify-content:center;gap:10px;margin-top:24px}
.footer-form .field{width:150px;height:26px;text-align:left}
.footer-form .go{width:70px;height:26px;background:var(--orange);font-family:"Raleway",sans-serif;font-weight:800;font-size:11px;display:flex;align-items:center;justify-content:center}
.footer-note{font-size:10px;margin-top:10px}
.social{display:flex;justify-content:center;gap:12px;margin-top:22px}
.social i{width:26px;height:26px;border-radius:50%;background:var(--yellow)}
.bottom-bar{position:absolute;top:2472px;left:0;width:1200px;height:36px;background:var(--night);color:#aaa;font-size:10px;display:flex;align-items:center;justify-content:space-between;padding:0 220px}
</style>
</head>
<body>
<header class="site-header">
  <div class="brand"><span>Marla Penrick</span><i class="brand-dot"></i></div>
  <nav class="main-nav"><span>EVENTS</span><span>WORK WITH ME</span><span>CORPORATE</span><span>ABOUT</span><span>CONTACT</span></nav>
</header>

<section class="hero" role="img" aria-label="Photo of the coach in a red dress standing before a bright blurred background"></section>
<div class="hero-copy">
  <h1 class="hero-title">ATTRACT CONNECT<span>INFLUENCE</span></h1>
  <p class="hero-text">I'm a charisma coach helping you shine, speak with ease and win people over every time.</p>
  <div class="hero-dots"><i></i><i></i><i></i><i></i></div>
</div>

<section class="signup-strap">
  <svg width="44" height="34" viewBox="0 0 44 34"><rect x="5" y="2" width="34" height="22" rx="2" fill="#fff"/><rect x="8" y="5" width="28" height="16" fill="#2a2a2a"/><path d="M17 10l7 3-7 3z" fill="#fff"/><rect x="0" y="26" width="44" height="4" rx="2" fill="#fff"/></svg>
  <div class="strap-copy"><strong>Learn how to unlock the superpower of your charisma and be the person everyone wants to listen to!</strong><small>*Free video series sent to inbox</small></div>
  <div class="strap-form"><div class="field">First name</div><div class="field">Email address</div></div>
  <div class="signup-btn">Sign<br>up</div>
</section>

<main class="blog-panel">
  <article class="post">
    <div class="post-banner banner-red"><div class="banner-copy">PUBLIC SPEAKING...<b>MADE EASY :-)</b></div><div class="banner-photo" role="img" aria-label="Photo of the coach speaking on stage" style="background:linear-gradient(135deg,#c7121a,#f06b5d)"></div></div>
    <h2 class="post-title">Public Speaking... made easy</h2>
    <p class="post-excerpt">Standing up in front of a room can feel terrifying, yet a few simple habits change everything. Here is how to breathe, pause and connect with every listener so your message lands with warmth and real confidence.</p>
    <div class="post-meta"><span class="read-more">READ MORE &gt;</span><span class="shares"><i></i><i></i><i></i></span></div>
  </article>
  <article class="post">
    <div class="post-banner banner-green"><div class="banner-copy">HOW TO START EVERY DAY IN THE RIGHT FRAME OF MIND!<b>5 HOT TIPS</b></div><div class="banner-photo" role="img" aria-label="Photo of the coach smiling" style="background:linear-gradient(135deg,#6aae35,#b7dd8a)"></div></div>
    <h2 class="post-title">How to start every day in the right frame of mind!</h2>
    <p class="post-excerpt">Your mornings set the tone for everything that follows. Try these five quick rituals to wake up energised, focused and ready to shine, whether you are pitching to clients or leading your own busy team today.</p>
    <div class="post-meta"><span class="read-more">READ MORE &gt;</span><span class="shares"><i></i><i></i><i></i></span></div>
  </article>
  <article class="post">
    <div class="post-banner banner-cyan"><div class="banner-copy">TAKE CHARGE OF YOUR STYLE... BOOST YOUR<b>CONFIDENCE</b></div><div class="banner-photo" role="img" aria-label="Photo of the coach posing in a stylish outfit" style="background:linear-gradient(135deg,#159fbd,#7fd5e6)"></div></div>
    <h2 class="post-title">Take charge of your style...Boost your confidence</h2>
    <p class="post-excerpt">What you wear speaks before you do. Learn how a small capsule wardrobe and a few bold choices can lift your presence, sharpen your first impression and make you feel ready for any room you walk into.</p>
    <div class="post-meta"><span class="read-more">READ MORE &gt;</span><span class="shares"><i></i><i></i><i></i></span></div>
  </article>
  <article class="post">
    <div class="post-banner banner-yellow"><div class="banner-copy">UNFULFILLED? IT'S TIME TO THINK ABOUT YOUR VALUES...<b style="font-size:24px">DO THIS EXERCISE NOW!</b></div><div class="banner-photo" role="img" aria-label="Photo of the coach gesturing while talking" style="background:linear-gradient(135deg,#e0b012,#f8de7a)"></div></div>
    <h2 class="post-title">Unfulfilled? It's time to think about your values...</h2>
    <p class="post-excerpt">When work feels flat, the reason is often a gap between what you do and what you value. This simple exercise helps you find what matters most and brings back the spark that people notice in you.</p>
    <div class="post-meta"><span class="read-more">READ MORE &gt;</span><span class="shares"><i></i><i></i><i></i></span></div>
  </article>
  <nav class="pagination"><span class="current">1</span><span>2</span><span>3</span><span>4</span><span>5</span><span>6</span><span>&gt;</span></nav>
</main>

<aside class="sidebar">
  <section class="widget">
    <h3 class="widget-title">TOP POSTS</h3>
    <ul class="top-list">
      <li>Three ways to own the room at your next event<em>READ MORE</em></li>
      <li>Why eye contact builds instant trust<em>READ MORE</em></li>
      <li>The power pose that calms your nerves<em>READ MORE</em></li>
      <li>Building rapport in under a minute<em>READ MORE</em></li>
      <li>Speak up and be heard in meetings<em>READ MORE</em></li>
    </ul>
  </section>
  <section class="widget">
    <h3 class="widget-title plain">TAGS</h3>
    <div class="tags"><span>charisma</span><span>capsule wardrobe</span><span>confidence</span><span>presence</span><span>power pose</span><span>speaking</span><span>style</span><span>rapport</span><span>values</span><span>mindset</span></div>
  </section>
  <section class="widget">
    <h3 class="widget-title plain">COMING UP</h3>
    <div class="event-card" role="img" aria-label="Photo of the coach presenting to a live audience">
      <div class="event-copy">UNLOCK THE SUPERPOWER OF CHARISMA<br><b>LIVE</b><small>London · Spring date</small></div>
      <div class="learn-more">LEARN MORE</div>
    </div>
  </section>
</aside>

<footer class="site-footer">
  <p class="footer-pitch">Hey! Don't go without signing up because you'll miss out on exclusive offers, awesome tips, and weekly motivation in my hot newsletter!</p>
  <div class="footer-form"><div class="field">Your name</div><div class="field">Email address</div><div class="go">SIGN UP</div></div>
  <p class="footer-note">I hate spam too – unsubscribe any time</p>
  <div class="social"><i></i><i></i><i></i><i></i><i></i></div>
</footer>
<div class="bottom-bar"><span>© Marla Penrick. All rights reserved.</span><span>Privacy Policy | Terms of Use | Disclaimer</span></div>
</body>
</html>
```